Up to the Challenge? Canadian based consulting company needs a two sided business card design

A Canadian based security risk management consulting company needs a two-sided business card design. What we do is provide advice and guidance related to emergency, security and business continuity management for small, medium and large companies to help ensure the protection of their people, assets, information, services, operations and reputation.

The final design should be simple, only one or two colours, eye catching, professional and one that makes people look at three or more times just because it looks so darn good.

I have include examples of business cards I like.

Target Market(s)

Small, medium and large companies.

Industry/Entity Type

Security

Contact Information for Business Card

Business Card Size: Standard size of 3.5" (89mm) x 2.0" (51mm) - (see full specifications and guides on PRINTA's website if required)
Card Stock: Looking to use PRINTA's Velda 32pt stock textured paper - seam colour either chili red or black
Business Name: The Harrowfield Group
Website: www.theharrowfieldgroup.example
Telephone: (555)214-0397
Name: Dana Forsythe
Position: Principle
e-mail: Dana.Forsythe@theharrowfieldgroup.example

Font styles to use
Serif

Colors
ec1f27
000000
9d9d9d
aaaaaa
606060

Requirements
Must have
• - "The Harrowfield Group" logo (see uploaded files). I have included grey scale and colour versions.
• - Business card details (as above)
Nice to have
• - One side black or grey scale.
• - Other side would likely be white.
• - Everyone likes the silver logo on the black background.
• - Small element of colour i.e. red but I'm leaning more to greyscale.
Should not have
• - A lot of colour. Keep it simple.

```html
<!DOCTYPE html>
<html lang="en">
<head>
<meta charset="utf-8">
<title>The Harrowfield Group – Business Card</title>
<link href="https://fonts.googleapis.com/css2?family=Cinzel:wght@400;600&family=Tinos:wght@400;700&family=Open+Sans:ital@1&display=swap" rel="stylesheet">
<style>
  :root {
    --backdrop: #4f4033;
    --card-white: #ffffff;
    --card-black: #0d0d0d;
    --ink-dark: #555555;
    --ink-mid: #606060;
    --ink-soft: #6a6a6a;
    --rule: #c4c4c4;
    --band-start: #4e4e50;
    --band-end: #7a7a7c;
  }
  * { box-sizing: border-box; margin: 0; padding: 0; }
  html, body { width: 1200px; height: 987px; overflow: hidden; }
  body { background: var(--backdrop); position: relative; }

  .card {
    position: absolute;
    left: 293px;
    width: 615px;
    height: 350px;
    box-shadow: 0 2px 6px rgba(0,0,0,.35);
  }
  .card--front { top: 130px; background: var(--card-white); }
  .card--back { top: 505px; background: var(--card-black); }

  /* front */
  .brand {
    position: absolute;
    left: 22px; width: 260px; top: 118px;
    text-align: center;
    font-family: "Cinzel", serif;
    font-weight: 600;
    color: var(--ink-mid);
  }
  .brand__mark {
    width: 34px; height: 34px; border-radius: 50%;
    background: var(--ink-mid);
    margin: 0 auto 14px;
  }
  .brand__name { font-size: 20px; letter-spacing: .5px; line-height: 1.15; }
  .brand__sub { font-size: 15px; letter-spacing: 3px; }

  .divider {
    position: absolute;
    left: 291px; top: 90px;
    width: 1px; height: 179px;
    background: var(--rule);
  }

  .contact {
    position: absolute;
    left: 314px; top: 94px;
    font-family: "Tinos", serif;
    color: var(--ink-dark);
    font-size: 15px;
    line-height: 1.45;
  }
  .contact__name {
    font-family: "Cinzel", serif;
    font-weight: 600;
    font-size: 23px;
    letter-spacing: .5px;
    color: var(--ink-dark);
    line-height: 1.2;
  }
  .contact__title { font-size: 16px; margin-bottom: 10px; }
  .contact__email { font-size: 14px; }
  .contact__web { margin-top: 10px; }
  .contact__label { font-weight: 700; }
  .contact__social { display: flex; align-items: center; gap: 6px; }
  .contact__social-box {
    width: 14px; height: 14px; background: var(--ink-dark); border-radius: 2px;
  }

  .footer-band {
    position: absolute;
    left: 0; bottom: 0;
    width: 100%; height: 25px;
    background: linear-gradient(90deg, var(--band-start), var(--band-end));
  }
  .footer-band__dot {
    position: absolute;
    left: 408px; top: 3px;
    width: 19px; height: 19px;
    border-radius: 50%;
    border: 1.5px solid var(--card-white);
  }

  /* back */
  .back-brand {
    position: absolute;
    left: 0; width: 100%; top: 88px;
    text-align: center;
    font-family: "Cinzel", serif;
    font-weight: 600;
    color: var(--ink-soft);
  }
  .back-brand__mark {
    width: 58px; height: 58px; border-radius: 50%;
    background: var(--ink-soft);
    margin: 0 auto 18px;
  }
  .back-brand__name { font-size: 28px; letter-spacing: 1px; line-height: 1.15; }
  .back-brand__sub { font-size: 20px; letter-spacing: 4px; }

  .back-web {
    position: absolute;
    left: 0; width: 100%; top: 290px;
    text-align: center;
    font-family: "Open Sans", sans-serif;
    font-style: italic;
    font-size: 15px;
    letter-spacing: 1px;
    color: var(--ink-dark);
  }
</style>
</head>
<body>
  <section class="card card--front">
    <div class="brand">
      <div class="brand__mark"></div>
      <div class="brand__name">THE HARROWFIELD</div>
      <div class="brand__sub">GROUP</div>
    </div>
    <div class="divider"></div>
    <div class="contact">
      <div class="contact__name">Dana Forsythe</div>
      <div class="contact__title">Principle</div>
      <div><span class="contact__label">P :</span> (555)214-0397</div>
      <div class="contact__email">Dana.Forsythe@theharrowfieldgroup.example</div>
      <div class="contact__web">www.theharrowfieldgroup.example</div>
      <div class="contact__social"><span class="contact__social-box"></span>adanaforsythe</div>
    </div>
    <div class="footer-band"><span class="footer-band__dot"></span></div>
  </section>

  <section class="card card--back">
    <div class="back-brand">
      <div class="back-brand__mark"></div>
      <div class="back-brand__name">THE HARROWFIELD</div>
      <div class="back-brand__sub">GROUP</div>
    </div>
    <div class="back-web">www.theharrowfieldgroup.example</div>
  </section>
</body>
</html>
```